Number of Website Pages Need Designing

I currently have a website design homepage already created, however I am looking for experience designer who can design a page for each of internal pages below which we can use to create the live design. The pages that require a design are:
Page 1- Contact us
Page 2 - About us
Page 3 - Blog
Page 4 - News
Page 5 - Product page, ie fleet insurance
Page 6 - Affiliate / Partners
Page 7 - Brokers page - You could create a page for this one from the information from this YouTube video: https://www.vidorama-example.net/watch?v=Qx4Lm8TzWp2
The design you create need to work with the same site colours, brand, font, look and feel of the site design attached,
You will need to cut and past the header and footer onto your designs so we can see the design fully
The link to our demo site is: https://snip-example.io/7RtKvNa
Please let us see your best designs
Any questions please us us know
Thank you

```html
<!DOCTYPE html>
<html lang="en">
<head>
<meta charset="utf-8">
<title>Corvano – Blog</title>
<link href="https://fonts.googleapis.com/css2?family=Poppins:wght@400;500;600;700&display=swap" rel="stylesheet">
<style>
:root{
  --navy:#052a44;
  --navy-deep:#06304f;
  --green:#1fbf5f;
  --ink:#0c2d45;
  --body:#5a6470;
  --white:#ffffff;
  --canvas:#ececec;
}
*{margin:0;padding:0;box-sizing:border-box}
html,body{width:1200px;height:2553px;overflow:hidden}
body{background:var(--canvas);font-family:'Poppins',sans-serif;color:var(--ink);position:relative}
.page{position:absolute;left:52px;top:52px;width:1090px;height:2482px;background:var(--white);overflow:hidden}
.abs{position:absolute}
/* header */
.site-header{left:0;top:0;width:1090px;height:99px;background:var(--navy)}
.brand{display:flex;align-items:center;gap:8px;color:var(--white);font-weight:600;font-size:26px;line-height:1}
.brand-dot{width:30px;height:30px;border-radius:50%;background:var(--green)}
.header-brand{left:111px;top:34px}
.nav{left:268px;top:42px;display:flex;gap:20px;font-size:12px;color:var(--white)}
.choose{left:775px;top:42px;font-size:12px;font-weight:600;color:var(--white)}
.login{left:903px;top:37px;width:78px;height:26px;border-radius:13px;background:var(--green);color:var(--white);font-size:12px;display:flex;align-items:center;justify-content:center;gap:6px}
/* hero */
.hero{left:0;top:99px;width:1090px;height:252px;background:linear-gradient(100deg,#0a4f6a,#0c6480 50%,#0a5068)}
.hero h1{position:absolute;left:0;right:0;top:96px;text-align:center;color:var(--white);font-size:30px;font-weight:700}
/* posts */
.photo{border-radius:16px}
.feature-photo{left:110px;top:413px;width:413px;height:567px;background:linear-gradient(160deg,#ddd5c9,#efdcd4 45%,#cdd3dc)}
.meta{font-size:13.5px;color:var(--green)}
.title{font-size:25px;font-weight:700;line-height:30px;color:var(--ink)}
.excerpt{font-size:14px;line-height:20.5px;color:var(--body)}
.feature{left:578px;top:409px;width:430px}
.feature .title{margin-top:12px}
.feature .excerpt{margin-top:12px;width:412px}
.feature h3{font-size:25px;font-weight:700;margin-top:15px;line-height:30px}
.feature ul{list-style:none;margin-top:16px;width:410px}
.feature li{position:relative;padding-left:14px;font-size:14px;line-height:20.5px;color:var(--body);margin-bottom:11px}
.feature li::before{content:"";position:absolute;left:0;top:8px;width:6px;height:6px;border-radius:50%;background:var(--green)}
.feature li b{color:var(--ink);font-weight:600}
.card{width:413px}
.card .photo{height:265px}
.card .meta{margin-top:24px}
.card .title{margin-top:12px}
.card .excerpt{margin-top:14px;width:412px}
.read-more{margin-top:16px;margin-left:1px;display:inline-flex;align-items:center;gap:8px;height:32px;padding:0 18px;border-radius:16px;background:var(--green);color:var(--white);font-weight:600;font-size:14px}
.vans{background:linear-gradient(170deg,#8d9aa1,#4f7d4e 55%,#7d8c86)}
.ai{background:radial-gradient(circle at 38% 45%,#3fc3e0 0,#165a7a 22%,#0c2c42 60%,#10283a)}
/* footer */
.site-footer{left:0;top:1688px;width:1090px;height:794px;background:radial-gradient(ellipse at 50% 70%,#0b3c63,var(--navy-deep) 70%)}
.footer-brand{left:66px;top:1742px;font-size:28px}
.footer-brand .brand-dot{width:34px;height:34px}
.follow{left:823px;top:1751px;font-size:12px;font-weight:600;color:var(--white)}
.socials{left:906px;top:1748px;display:flex;gap:7px}
.socials span{width:25px;height:25px;border-radius:50%;background:var(--white)}
.fcol{color:var(--white);font-size:12px;line-height:17.7px;width:205px}
.fcol h4{font-size:12px;font-weight:600;margin-bottom:10px}
.tagline{left:651px;top:2339px;font-size:14.5px;color:var(--white);font-weight:500}
.tagline em{font-style:normal;color:var(--green)}
.tagline-rule{left:151px;top:2365px;width:714px;height:2px;background:var(--green)}
.legal{left:0;top:2383px;width:1090px;text-align:center;font-size:8.5px;line-height:14.5px;color:var(--white);white-space:nowrap}
.copyright{left:0;top:2431px;width:1090px;text-align:center;font-size:13px;color:var(--white)}
</style>
</head>
<body>
<div class="page">
  <header class="site-header abs">
    <div class="brand header-brand abs"><span class="brand-dot"></span>corvano</div>
    <nav class="nav abs"><span>Home</span><span>How it works</span><span>Products</span><span>FAQs</span><span>About</span></nav>
    <div class="choose abs">Choose a Product</div>
    <div class="login abs">Login
      <svg width="9" height="9" viewBox="0 0 10 10"><path d="M2 8 8 2M3 2h5v5" stroke="#fff" stroke-width="1.4" fill="none"/></svg>
    </div>
  </header>

  <section class="hero abs" role="img" aria-label="Couple smiling together at a laptop, blue-tinted">
    <h1>Blog</h1>
  </section>

  <div class="feature-photo photo abs" role="img" aria-label="Woman smiling while using her phone at a desk"></div>
  <article class="feature abs">
    <div class="meta">Mar 31, 2025 | Uncategorised</div>
    <h2 class="title">Embedded Insurance: Seamless Protection</h2>
    <p class="excerpt">Embedded insurance—insurance integrated into the purchase of a product or service—is reshaping how consumers buy coverage in 2025. Picture buying a phone and getting a protection plan in one click.</p>
    <h3>The Appeal</h3>
    <ul>
      <li><b>Convenience:</b> No separate shopping—insurance is part of the checkout process.</li>
      <li><b>Partnerships:</b> Insurtechs team up with e-commerce giants, travel platforms, and even car dealerships.</li>
      <li><b>Micro-Policies:</b> Short-term, affordable options tailored to specific needs, like a weekend trip.</li>
    </ul>
    <h3>Growth Stats</h3>
    <ul>
      <li>Embedded insurance hit $50B in global premiums last year, doubling since 2023.</li>
      <li>70% of millennials say they’d buy insurance this way, per surveys.</li>
    </ul>
  </article>

  <article class="card abs" style="left:110px;top:1045px">
    <div class="photo vans" role="img" aria-label="Fleet of green branded vans parked in a city street"></div>
    <div class="meta">Mar 31, 2025 | Uncategorised</div>
    <h2 class="title">Parametric Insurance: The Next Frontier</h2>
    <p class="excerpt">Parametric insurance is gaining traction in 2025, offering a payout model based on predefined triggers rather than traditional loss assessments....</p>
    <span class="read-more">Read More <svg width="11" height="11" viewBox="0 0 10 10"><path d="M2 8 8 2M3 2h5v5" stroke="#fff" stroke-width="1.4" fill="none"/></svg></span>
  </article>

  <article class="card abs" style="left:578px;top:1045px">
    <div class="photo ai" role="img" aria-label="Glowing AI hologram above a smartphone held in a hand"></div>
    <div class="meta">Mar 31, 2025 | Uncategorised</div>
    <h2 class="title">The Rise of AI in Claims Processing</h2>
    <p class="excerpt">Parametric insurance is gaining traction in 2025, offering a payout model based on predefined triggers rather than traditional loss assessments....</p>
    <span class="read-more">Read More <svg width="11" height="11" viewBox="0 0 10 10"><path d="M2 8 8 2M3 2h5v5" stroke="#fff" stroke-width="1.4" fill="none"/></svg></span>
  </article>

  <footer class="site-footer abs"></footer>
  <div class="brand footer-brand abs"><span class="brand-dot"></span>corvano</div>
  <div class="follow abs">Follow Us</div>
  <div class="socials abs"><span></span><span></span><span></span><span></span></div>

  <div class="fcol abs" style="left:66px;top:1840px;width:220px">
    <h4>United Kingdom Office</h4>
    <p>Ashby House, 14 Linden Road,<br>Ledwell,<br>Harfordshire,<br>United Kingdom,<br>LW9 4QT</p>
    <p style="margin-top:26px">Email Address:<br>support@corvano.example</p>
  </div>
  <div class="fcol abs" style="left:321px;top:1840px">
    <h4>Services</h4>
    <p>All Services<br>Staffing Services<br>Direct Placement<br>Executive Recruiting<br>Recruitment Process Outsourcing (RPO)<br>Long-Term Project Support<br>Workplace Culture Advice<br>Hire Someone</p>
  </div>
  <div class="fcol abs" style="left:577px;top:1840px">
    <h4>Resources</h4>
    <p>Consultants<br>Find a Job<br>Time &amp; Expense Approval<br>Timesheet Printout<br>Employment Verification<br>In-House Team<br>Join Our In-House Team<br>Community Outreach<br>Job Index</p>
  </div>
  <div class="fcol abs" style="left:577px;top:2069px">
    <h4>Partnerships</h4>
    <p>Join our providers panel<br>Affiliates<br>Research &amp; Development Partner</p>
  </div>
  <div class="fcol abs" style="left:833px;top:1840px;width:205px">
    <h4>Information</h4>
    <p>About<br>ESG<br>Veterans<br>Blog<br>Newsroom<br>Contact<br>Office Locations<br>Complete Guides<br>Videos &amp; Events<br>Resources<br>Privacy Policy<br>Workforce Privacy Policy<br>Ontario AODA/Accessibility Policy<br>Do Not Sell or Share My Personal Info<br>Consumer Rights Requests<br>Transparency in Coverage<br>Terms of Use<br>Sitemap<br>Corporate Ethics Hotline<br>Anti Racism Statement<br>Compliance Program Policies<br>Consumer Alerts</p>
  </div>

  <div class="tagline abs">Insurance The <em>Corvano</em> Way!</div>
  <div class="tagline-rule abs"></div>
  <p class="legal abs">Corvano is a trading style of Northfield Tech Group Limited who are a registered company in England and Wales. Registered number: 19004412.<br>Authorised and regulated by the Financial Standards Authority under Firm Reference Number 1073319. This can be checked on the Financial Services Register at www.fsa-register.example/register.</p>
  <div class="copyright abs">Copyright © 2025 All Rights Reserved</div>
</div>
</body>
</html>
```